Chiropractic healthcare group business card

We are a Portland Oregon based chiropractic healthcare group. Looking for a new business card design. Something cutting edge, that shows off our new logo and tag line.Use either of the attached logos.Our tag line = "Who would you be without pain?"I'm open to about anything, impress me!!
Target Market(s)
Chiropractic patients - Auto injury, back pain, sports injuries, neck , shoulder, hip, knee, ankle pain.
Industry/Entity Type
Chiropractic
Contact Information for Business Card
Dr. Bram Holtvick, D.C.
Clinic name - Fernway Chiropractic
2 clinics
location #1
20418 NW Marwick Road
Suite B
North Plains, OR 97133
Location #2
13529 SE Calloway Street
Portland OR 97236
Main phone line 971.555.0143
website : www.FernwayClinics.example
Tag line "Who would you be without pain?"
Colors
Designer to choose colors to be used in the design.
Requirements
Must have
- Use the logo colors -- Want the orange color to be a TRUE orange.
- Both clinic address
- phone number
- website
- personal email - b.holtvick@ReliefBeginsHere.example
- tag line - "Who would you be without pain?"

```html
<!DOCTYPE html>
<html lang="en">
<head>
<meta charset="utf-8">
<title>Fernway Chiropractic – Business Card</title>
<link rel="stylesheet" href="https://fonts.googleapis.com/css2?family=Didact+Gothic&family=Montserrat:wght@600&display=swap">
<style>
  :root {
    --orange: #f7851f;
    --card-dark: #252525;
    --strip-dark: #1d1d1d;
    --mark-grey: #5a5a5a;
    --text-light: #d9d9d9;
    --white: #ffffff;
    --backdrop: #eef1f2;
  }
  * { box-sizing: border-box; margin: 0; padding: 0; }
  html, body { width: 1200px; height: 900px; overflow: hidden; }
  body {
    background: var(--backdrop);
    font-family: "Didact Gothic", "Century Gothic", sans-serif;
    position: relative;
  }
  .card {
    position: absolute;
    left: 250px;
    width: 700px;
    height: 400px;
    background: var(--card-dark);
    border: 5px solid var(--orange);
    overflow: hidden;
    box-shadow: 0 6px 18px rgba(0,0,0,0.18);
  }
  .card--front { top: 40px; }
  .card--back { top: 460px; }

  /* Front */
  .front__top-strip { position: absolute; left: 0; right: 0; top: 0; height: 22px; background: var(--strip-dark); }
  .front__band {
    position: absolute; left: 0; right: 0; top: 22px; height: 36px;
    background: var(--orange);
    display: flex; align-items: center; padding-left: 26px;
  }
  .tagline { color: var(--white); font-size: 17px; letter-spacing: 0.5px; }
  .brand-lockup {
    position: absolute; left: 0; right: 0; top: 185px;
    display: flex; align-items: center; justify-content: center; gap: 14px;
  }
  .brand-lockup__square { width: 22px; height: 22px; background: var(--orange); }
  .brand-lockup__name {
    color: var(--mark-grey); font-size: 34px; letter-spacing: 3px;
  }

  /* Back */
  .back__identity { position: absolute; left: 48px; top: 44px; }
  .back__name {
    font-family: "Montserrat", sans-serif; font-weight: 600;
    color: var(--orange); font-size: 30px;
  }
  .back__clinic { color: var(--text-light); font-size: 17px; margin-top: 4px; }
  .contact-list { position: absolute; left: 48px; top: 140px; list-style: none; }
  .contact-list__item {
    display: flex; align-items: flex-start; gap: 14px;
    color: var(--text-light); font-size: 15px; line-height: 1.3;
    margin-bottom: 10px;
  }
  .contact-list__icon { width: 18px; height: 18px; flex: none; margin-top: 1px; }
  .back__mark {
    position: absolute; right: 40px; top: 70px;
    display: flex; align-items: center; gap: 12px;
  }
  .back__mark-name { color: var(--orange); font-size: 24px; letter-spacing: 1px; }
  .back__mark-square { width: 18px; height: 18px; background: var(--mark-grey); }
  .back__band {
    position: absolute; left: 0; right: 0; bottom: 22px; height: 36px;
    background: var(--orange);
    display: flex; align-items: center; justify-content: flex-end; padding-right: 26px;
  }
  .website { color: var(--white); font-size: 17px; letter-spacing: 0.5px; }
  .back__bottom-strip { position: absolute; left: 0; right: 0; bottom: 0; height: 22px; background: var(--strip-dark); }
</style>
</head>
<body>

<section class="card card--front" aria-label="Card front">
  <div class="front__top-strip"></div>
  <div class="front__band"><p class="tagline">“Who would you be without pain?”</p></div>
  <div class="brand-lockup">
    <span class="brand-lockup__square"></span>
    <span class="brand-lockup__name">Fernway Chiropractic</span>
  </div>
</section>

<section class="card card--back" aria-label="Card back">
  <div class="back__identity">
    <h1 class="back__name">Dr. Bram Holtvick (D.C)</h1>
    <p class="back__clinic">Clinic : Fernway Chiropractic</p>
  </div>

  <ul class="contact-list">
    <li class="contact-list__item">
      <svg class="contact-list__icon" viewBox="0 0 24 24" aria-hidden="true"><path fill="#f7851f" d="M6.6 10.8a15 15 0 0 0 6.6 6.6l2.2-2.2c.3-.3.7-.4 1-.2 1.1.4 2.3.6 3.6.6.6 0 1 .4 1 1V20c0 .6-.4 1-1 1A17 17 0 0 1 3 4c0-.6.4-1 1-1h3.5c.6 0 1 .4 1 1 0 1.3.2 2.5.6 3.6.1.3 0 .7-.2 1z"/></svg>
      <span>971.555.0143</span>
    </li>
    <li class="contact-list__item">
      <svg class="contact-list__icon" viewBox="0 0 24 24" aria-hidden="true"><path fill="#f7851f" d="M12 2a7 7 0 0 0-7 7c0 5 7 13 7 13s7-8 7-13a7 7 0 0 0-7-7zm0 9.5A2.5 2.5 0 1 1 12 6.5a2.5 2.5 0 0 1 0 5z"/></svg>
      <span>13529 SE Calloway Street<br>Portland OR 97236</span>
    </li>
    <li class="contact-list__item">
      <svg class="contact-list__icon" viewBox="0 0 24 24" aria-hidden="true"><path fill="#f7851f" d="M12 2a7 7 0 0 0-7 7c0 5 7 13 7 13s7-8 7-13a7 7 0 0 0-7-7zm0 9.5A2.5 2.5 0 1 1 12 6.5a2.5 2.5 0 0 1 0 5z"/></svg>
      <span>20418 NW Marwick Road<br>suite B, North Plains, OR 97133</span>
    </li>
    <li class="contact-list__item">
      <svg class="contact-list__icon" viewBox="0 0 24 24" aria-hidden="true"><path fill="#f7851f" d="M2 5h20v14H2zm2 2v.5l8 5 8-5V7l-8 5z"/></svg>
      <span>b.holtvick@ReliefBeginsHere.example</span>
    </li>
  </ul>

  <div class="back__mark">
    <span class="back__mark-square"></span>
    <span class="back__mark-name">Fernway Chiropractic</span>
  </div>

  <div class="back__band"><p class="website">www.FernwayClinics.example</p></div>
  <div class="back__bottom-strip"></div>
</section>

</body>
</html>
```